Business Card Ayurvedic Massage

I'm starting with my ayurvedic massage business and need a business card design. The design should be inline with my brand/logo as well as with the design of my website (www.lumo-thara.ch).
Front: logo and text "Ayurvedische Massagen"
back: name and adress (see details https://www.lumo-thara.ch/kontakt.html)

```html
<!DOCTYPE html>
<html lang="de">
<head>
<meta charset="utf-8">
<title>lumo-thara – Visitenkarte</title>
<link rel="stylesheet" href="https://fonts.googleapis.com/css2?family=Crimson+Text:ital,wght@0,400;0,600;0,700;1,400&family=Yatra+One&display=swap">
<style>
  :root {
    --stage: #2a2a2c;
    --card-red: #8e1414;
    --card-red-deep: #6f0c0c;
    --gold: #f0c25a;
    --gold-soft: #e7b876;
    --cream: #f6dcae;
    --photo-warm: #d2561c;
    --photo-glow: #f59a3a;
  }
  * { box-sizing: border-box; margin: 0; padding: 0; }
  html, body {
    width: 1200px; height: 880px; overflow: hidden;
    background: var(--stage);
  }
  .stage {
    width: 1200px; height: 880px;
    display: flex; flex-direction: column; align-items: center; justify-content: center;
    gap: 44px;
  }
  .card {
    position: relative;
    width: 600px; height: 360px;
    border-radius: 22px;
    overflow: hidden;
    background: radial-gradient(ellipse at 55% 45%, var(--card-red) 0%, var(--card-red-deep) 100%);
    box-shadow: 0 14px 30px rgba(0,0,0,.45);
  }
  /* front */
  .front__monument {
    position: absolute; inset: 0;
    background: radial-gradient(ellipse at 55% 42%, rgba(160,40,30,.55) 0%, rgba(120,20,18,0) 65%);
  }
  .front__brand {
    position: absolute; left: 0; right: 0; top: 128px;
    display: flex; flex-direction: column; align-items: center; gap: 14px;
  }
  .brand-name {
    display: flex; align-items: center; gap: 14px;
    font-family: "Crimson Text", serif; font-weight: 600;
    font-size: 54px; color: var(--gold); letter-spacing: 1px;
  }
  .brand-name__dot {
    width: 18px; height: 18px; border-radius: 50%; background: var(--gold);
  }
  .brand-tagline {
    font-family: "Crimson Text", serif; font-size: 19px;
    letter-spacing: 3px; text-transform: uppercase; color: var(--gold-soft);
  }
  /* back */
  .back__photo {
    position: absolute; right: 0; top: 0; width: 78%; height: 78%;
    background:
      radial-gradient(circle at 72% 30%, var(--photo-glow) 0%, rgba(245,154,58,0) 32%),
      linear-gradient(160deg, rgba(210,86,28,.85) 0%, rgba(160,40,20,.6) 55%, rgba(142,20,20,0) 100%);
    border-bottom-left-radius: 60% 40%;
  }
  .back__contact {
    position: absolute; left: 0; right: 0; top: 118px;
    display: flex; flex-direction: column; align-items: center;
    text-align: center; color: var(--cream);
    font-family: "Crimson Text", serif;
  }
  .contact-name {
    font-family: "Yatra One", serif; font-size: 44px; color: var(--gold);
    line-height: 1;
  }
  .contact-role { font-size: 17px; margin-top: 2px; margin-bottom: 22px; }
  .contact-line { font-size: 16px; line-height: 1.55; }
  .contact-line b { font-weight: 700; }
  .contact-web { font-size: 17px; font-style: italic; margin-top: 2px; }
  .contact-web b { font-style: normal; font-weight: 700; letter-spacing: 1px; }
</style>
</head>
<body>
<main class="stage">
  <section class="card front">
    <div class="front__monument" role="img" aria-label="Faint illustration of a domed Indian palace with minarets"></div>
    <div class="front__brand">
      <div class="brand-name"><span class="brand-name__dot"></span>lumo-thara</div>
      <div class="brand-tagline">Ayurvedische Massagen</div>
    </div>
  </section>

  <section class="card back">
    <div class="back__photo" role="img" aria-label="Warm candlelit photo of a massage room with flowers on the table"></div>
    <div class="back__contact">
      <div class="contact-name">Lena Brandt</div>
      <div class="contact-role">Manager</div>
      <div class="contact-line"><b>Mobile:</b> +41 77 000 12 34 | <b>Email:</b> info@lumo-thara.ch</div>
      <div class="contact-line">Mira Kaelin, lumo-thara, Lindenweg 14, 8000 Musterdorf (SZ)</div>
      <div class="contact-web">www.<b>lumo-thara</b>.ch</div>
    </div>
  </section>
</main>
</body>
</html>
```